Economic Development Consulting needs killer brochure for National Civic Design Society Conference

Brightwater Advisors is an elite sponsor for the NCDS conference this year. Our Three service offerings for the event are
Economic Development Master Planning (and our proprietary approach)
Feasibility Studies and Site Options Analysis (also leverages our proprietary approach)
Resilience Assessment & Planning
Our slogan is Customized consulting for communities and community planners and Uncommon Insights — Aligning Resources to Opportunity

We need a square, trifold brochure, and we would like 3 posters, one dedicated to each of our service offerings, matching the brochure.

The NCDS conference site is http://www.ncdsfrontier.org/annual-conference
Updates

We have increased the budget for the brochure requested. The posters referenced int eh posting will be a separate project, offered to the designer who designs the brochure.

Reason: We are looking at adding some additional text.

Target Market(s)

Planners, Architects,

Industry/Entity Type

Consulting

Font styles to use
Sans Serif

Colors
0255a3

Requirements
Must have
• Square, trifold

```html
<!DOCTYPE html>
<html lang="en">
<head>
<meta charset="utf-8">
<title>Feasibility Studies and Site Options Analysis — Brightwater Advisors</title>
<link href="https://fonts.googleapis.com/css2?family=Cabin:wght@400;500;700&display=swap" rel="stylesheet">
<style>
  :root {
    --brand-blue: #4a6aa8;
    --brand-deep: #0255a3;
    --ink-blue: #1f4e9a;
    --paper: #ffffff;
    --accent-grey: #b9bfcb;
  }
  html, body {
    margin: 0;
    padding: 0;
    width: 1200px;
    height: 1173px;
    overflow: hidden;
    background: var(--paper);
  }
  .poster {
    position: relative;
    width: 1200px;
    height: 1173px;
    overflow: hidden;
    background: var(--paper);
    font-family: "Cabin", sans-serif;
  }
  .title-band {
    position: absolute;
    left: 0; top: 0;
    width: 1200px; height: 180px;
    background: var(--brand-blue);
    display: flex;
    align-items: center;
    justify-content: center;
  }
  .title-band h1 {
    margin: 0;
    color: var(--paper);
    font-weight: 400;
    font-size: 37px;
    letter-spacing: 0.4px;
    padding-bottom: 8px;
    white-space: nowrap;
  }
  .hero {
    position: absolute;
    left: 0; top: 180px;
    width: 1200px; height: 810px;
  }
  .hero svg { display: block; }
  .services {
    position: absolute;
    left: 90px; top: 1000px;
    margin: 0; padding: 0;
    list-style: none;
    color: var(--ink-blue);
    font-size: 27px;
  }
  .services li {
    position: relative;
    padding-left: 32px;
    height: 54px;
    line-height: 46px;
    white-space: nowrap;
  }
  .services li::before {
    content: "\2605";
    position: absolute;
    left: 0;
    font-size: 17px;
    color: var(--ink-blue);
  }
  .brand-name {
    position: absolute;
    left: 900px; top: 1030px;
    width: 220px;
    text-align: center;
    color: var(--brand-deep);
    font-weight: 700;
    font-size: 28px;
    line-height: 1.05;
    letter-spacing: 0.5px;
  }
  .brand-name .mark {
    display: block;
    width: 50px; height: 50px;
    margin: 0 auto 14px;
    border-radius: 50%;
    background: var(--brand-deep);
  }
</style>
</head>
<body>
<main class="poster">
  <header class="title-band">
    <h1>FEASIBILITY STUDIES AND SITE OPTIONS ANALYSIS</h1>
  </header>

  <section class="hero">
    <svg width="1200" height="810" viewBox="0 0 1200 810">
      <defs>
        <linearGradient id="heroTone" x1="0" y1="0" x2="1" y2="1">
          <stop offset="0" stop-color="#5f8fc6"/>
          <stop offset="0.35" stop-color="#c9a692"/>
          <stop offset="0.6" stop-color="#a87a68"/>
          <stop offset="0.85" stop-color="#5f80aa"/>
          <stop offset="1" stop-color="#4d76b0"/>
        </linearGradient>
      </defs>
      <rect class="hero-photo" x="0" y="0" width="1200" height="810" fill="url(#heroTone)"
            role="img" aria-label="Photograph of a person looking up at the sky through opera glasses"/>
      <g class="diagonal-bands">
        <polygon points="0,0 330,0 0,420" fill="#1f4e9a" opacity="0.55"/>
        <polygon points="470,0 560,0 0,720 0,600" fill="#ffffff" opacity="0.35"/>
        <polygon points="860,0 1020,0 380,810 220,810" fill="#1f4e9a" opacity="0.35"/>
        <polygon points="1060,0 1200,0 1200,40 580,810 440,810" fill="#0b1f4a" opacity="0.5"/>
        <polygon points="1200,160 1200,330 820,810 690,810" fill="#0b1f4a" opacity="0.55"/>
      </g>
      <rect class="base-panel" x="0" y="700" width="1000" height="110" fill="#4a6aa8"/>
      <rect class="base-square" x="1018" y="760" width="40" height="50" fill="#b9bfcb"/>
    </svg>
  </section>

  <ul class="services">
    <li>Comprehensive analysis of current state and options</li>
    <li>Statistical modeling tool creates best fit scenarios</li>
    <li>Strategic planning for current and future use</li>
  </ul>

  <div class="brand-name">
    <span class="mark"></span>
    BRIGHTWATER<br>ADVISORS
  </div>
</main>
</body>
</html>
```